Visitenkarte für Ergotherapiepraxis
Zielgruppe
Wir arbeiten mit Kindern und Erwachsene jeden Alters.
Diese Personen kommen mit Beeinträchtigungen (körperlich, seelisch, schulisch) im täglichen Leben zu uns. Wir unterstützen unsere Patienten die Beeinträchtigungen zu verringern oder zu kompensieren und so den Alltag besser bewältigen zu können.
Aufgabenstellung
Ein Design was Kinder und Erwachsene anspricht, aber nicht zu verspielt wirkt. Es soll vertrauenserweckend sein. Eventuell sollte die Visitenkarte ein "aufgehendes oder erblühendes oder aufsteigendes" Element enthalten (=zu Beginn war die Beeinträchtigung dann steigt die Lebensqualität als Folge der Behandlung)
Daten vorn:
Ergotherapiepraxis

```html
<!DOCTYPE html>
<html lang="de">
<head>
<meta charset="utf-8">
<title>Visitenkarte Ergotherapie Praxis</title>
<link href="https://fonts.googleapis.com/css2?family=Ubuntu:wght@300;400;500&display=swap" rel="stylesheet">
<style>
  :root {
    --orange: #ff6a00;
    --ink: #1f1f1f;
    --text: #2b2b2b;
    --white: #ffffff;
    --stage-light: #ffffff;
    --stage-dark: #d9d9d9;
    --card-light: #ffffff;
    --card-edge: #d8d8d8;
    --card-border: #c9c9c9;
  }
  * { margin: 0; padding: 0; box-sizing: border-box; }
  html, body { width: 1200px; height: 1040px; overflow: hidden; }
  body {
    position: relative;
    font-family: "Ubuntu", sans-serif;
    background: radial-gradient(ellipse at 50% 50%, var(--stage-light) 30%, var(--stage-dark) 100%);
  }
  .card {
    position: absolute;
    top: 188px;
    width: 359px;
    height: 628px;
    text-align: center;
  }
  .card--back {
    left: 222px;
    background: var(--orange);
    color: var(--white);
  }
  .card--front {
    left: 599px;
    background: radial-gradient(ellipse at 50% 50%, var(--card-light) 25%, var(--card-edge) 100%);
    border: 1px solid var(--card-border);
    color: var(--text);
  }
  .role-title {
    position: absolute; top: 36px; left: 0; right: 0;
    font-weight: 300; font-size: 37px; line-height: 44px; letter-spacing: 0.5px;
  }
  .practice-title {
    position: absolute; top: 36px; left: 0; right: 0;
    font-weight: 500; font-size: 36px; line-height: 44px; color: var(--ink);
  }
  .practice-owner {
    position: absolute; top: 135px; left: 0; right: 0;
    font-size: 20px; color: var(--ink);
  }
  .brand-mark {
    position: absolute; left: 0; right: 0;
    display: flex; align-items: center; justify-content: center; gap: 12px;
    font-weight: 500;
  }
  .card--back .brand-mark { top: 250px; font-size: 40px; color: var(--white); }
  .card--front .brand-mark { top: 282px; font-size: 30px; color: var(--orange); }
  .brand-dot { border-radius: 50%; display: inline-block; }
  .card--back .brand-dot { width: 24px; height: 24px; background: var(--white); }
  .card--front .brand-dot { width: 18px; height: 18px; background: var(--orange); }
  .therapist-name {
    position: absolute; top: 562px; left: 0; right: 0;
    font-size: 20px;
  }
  .address {
    position: absolute; top: 448px; left: 0; right: 0;
    font-size: 23px; line-height: 43px; color: var(--text);
  }
  .phone-band {
    position: absolute; left: -1px; right: -1px; bottom: -1px; height: 63px;
    background: var(--orange); color: var(--white);
    font-size: 40px; line-height: 63px; font-weight: 400;
  }
</style>
</head>
<body>
  <section class="card card--back">
    <h2 class="role-title">BEHANDELNDER<br>Therapeut</h2>
    <div class="brand-mark"><span class="brand-dot"></span>VOGT</div>
    <p class="therapist-name">MARLENE VOGT</p>
  </section>

  <section class="card card--front">
    <h1 class="practice-title">ERGOTHERAPIE<br>Praxis</h1>
    <p class="practice-owner">MARLENE VOGT</p>
    <div class="brand-mark"><span class="brand-dot"></span>VOGT</div>
    <p class="address">Am Lindenhang | Hof 4<br>14820 Birkenau, OT Wiese</p>
    <p class="phone-band">033482/51907</p>
  </section>
</body>
</html>
```